PLOR-Increasing Social Capital

The attached white paper is a research planning grant proposal. I would like to take the key elements and make a pwrpt presentation to be used at an upcoming conference. Can you digest the paper and create me a summary using my TB7UM color designs but use the content from the research paper. If you have questions let me know.

Social

```html
<!DOCTYPE html>
<html lang="en">
<head>
<meta charset="utf-8">
<title>Survey and Observation Tools</title>
<link href="https://fonts.googleapis.com/css2?family=Roboto:wght@700&family=Open+Sans:wght@400;500&display=swap" rel="stylesheet">
<style>
  :root {
    --page: #ffffff;
    --panel: #2e74b5;
    --ink: #ffffff;
    --sky-top: #4a6a96;
    --sky-mid: #8fb4e6;
    --ground: #5b6f8a;
    --ground-dark: #2c3a50;
  }
  html, body {
    margin: 0;
    padding: 0;
    width: 1200px;
    height: 677px;
    overflow: hidden;
    background: var(--page);
  }
  .slide {
    position: relative;
    width: 1200px;
    height: 677px;
    background: var(--page);
  }
  .field-photo {
    position: absolute;
    left: 4px;
    top: 4px;
    width: 384px;
    height: 668px;
    background: linear-gradient(180deg,
      var(--sky-top) 0%,
      #6f8fbf 25%,
      var(--sky-mid) 50%,
      var(--ground) 62%,
      #7588a3 75%,
      var(--ground-dark) 100%);
  }
  .content-panel {
    position: absolute;
    left: 388px;
    top: 4px;
    width: 808px;
    height: 668px;
    background: var(--panel);
    color: var(--ink);
  }
  .slide-title {
    position: absolute;
    left: 64px;
    top: 38px;
    margin: 0;
    font-family: "Roboto", Arial, sans-serif;
    font-weight: 700;
    font-size: 52px;
    line-height: 61px;
    letter-spacing: 0.2px;
  }
  .slide-body {
    position: absolute;
    left: 64px;
    top: 187px;
    width: 672px;
    margin: 0;
    font-family: "Open Sans", Calibri, sans-serif;
    font-weight: 500;
    font-size: 17.6px;
    line-height: 27.2px;
    text-align: justify;
  }
  .slide-body .marked {
    text-decoration: underline;
    text-decoration-color: #e05050;
    text-decoration-style: wavy;
    text-decoration-thickness: 1px;
  }
</style>
</head>
<body>
  <div class="slide">
    <div class="field-photo" role="img" aria-label="Surveyor with a hat looking through a tripod-mounted instrument in a grassy desert plain, with a tall rock formation under a cloudy sky, blue-tinted"></div>
    <section class="content-panel">
      <h1 class="slide-title">SURVEY AND<br>OBSERVATION TOOLS</h1>
      <p class="slide-body">Several survey instruments will be developed as part of the evaluation process, these include community, teachers, and student surveys. Additionally, to evaluate the appearance of the five Social Capital Rural Education <span class="marked">Education</span> / Administration Place Based Models Organizational Change Decision Making&nbsp; Professional Practice 15 broad interconnected components of EL3, rubrics have been developed to assist in understanding the appearance, activities, and participation of each component. The rubrics will be evaluated by key PLOR personnel and will establish measures for each component and participant. These rubrics are attached below.</p>
    </section>
  </div>
</body>
</html>
```